Payroll Brochure

Create a brochure with the copy i have provided . A simple easy tp read brochure that shows wat we do we handle payroll taxes insurance 401k etc

```html
<!DOCTYPE html>
<html lang="en">
<head>
<meta charset="utf-8">
<title>Payroll Services Brochure</title>
<link rel="stylesheet" href="https://fonts.googleapis.com/css2?family=Cinzel:wght@700&family=Playfair+Display:ital,wght@1,700&family=Source+Serif+4:wght@300&display=swap">
<style>
  :root {
    --sun: #fcf336;
    --sun-deep: #e4db3c;
    --sun-shade: #d8cf44;
    --ink: #1c1c14;
  }
  * { margin: 0; padding: 0; box-sizing: border-box; }
  html, body { width: 1200px; height: 927px; overflow: hidden; background: var(--sun); }
  .brochure {
    position: relative;
    width: 1200px;
    height: 927px;
    background: var(--sun);
    color: var(--ink);
    font-family: "Source Serif 4", Georgia, serif;
    font-weight: 300;
    font-size: 12.2px;
    line-height: 15.9px;
    letter-spacing: 0.45px;
    font-variant-numeric: oldstyle-nums;
  }
  .photo-band {
    position: absolute;
    left: 399px;
    top: 0;
    width: 401px;
    height: 927px;
    background: radial-gradient(ellipse at 55% 30%, var(--sun-shade), var(--sun-deep) 60%, var(--sun-deep));
  }
  .panel {
    position: absolute;
    top: 26px;
    width: 370px;
  }
  .panel--left { left: 12px; }
  .panel--middle { left: 415px; }
  .panel--right { left: 817px; }
  .section-title {
    font-family: "Cinzel", "Times New Roman", serif;
    font-weight: 700;
    font-size: 13.5px;
    letter-spacing: 2.4px;
    text-align: center;
    line-height: 18px;
    white-space: nowrap;
    margin: 14px 0 14px;
  }
  .section-title:first-child { margin-top: 0; }
  .feature {
    text-align: justify;
    margin-bottom: 16px;
  }
  .feature:last-child { margin-bottom: 0; }
  .feature-name {
    font-family: "Playfair Display", Georgia, serif;
    font-style: italic;
    font-weight: 700;
  }
</style>
</head>
<body>
<main class="brochure">
  <div class="photo-band" role="img" aria-label="Faint photograph of a smiling team tinted in yellow"></div>

  <section class="panel panel--left">
    <h2 class="section-title">PAYROLL</h2>
    <p class="feature"><span class="feature-name">Flexible</span> – NORVALE’S flexible and powerful payroll module allows you the availability to grow you’re your business by meeting your unique needs. Supporting payrolls for very large to very small companies</p>
    <p class="feature"><span class="feature-name">Efficient</span> – Get payroll done efficiently and accurately by relying on your flexible design to handle even the most complex payroll needs.</p>
    <p class="feature"><span class="feature-name">Grow without Growing Pains</span> – NORVALE’S technology and design is able to allow you to scale your business without adding all the incremental costs typically required.</p>

    <h2 class="section-title">TAX REPORTING &amp; PAYMENTS</h2>
    <p class="feature"><span class="feature-name">Accurate</span> – all payroll taxes (federal, state, local) are calculated accurately. Additionally, we determine proper local tax jurisdictions based on the employee home and work addresses.</p>
    <p class="feature"><span class="feature-name">Complete</span> – Federal, State, and Local withholding taxes as well as State and Federal Unemployment taxes are provided. Tax payments are integrated into the Accounts Payable and General Ledger modules.</p>

    <h2 class="section-title">HUMAN RESOURCES</h2>
    <p class="feature">With our online HR tools, you can empower yourself to take control of your human resource needs or let us do it.</p>
    <p class="feature"><span class="feature-name">Get Big Company Services</span> – by using our online tools in conjunction with your service team, you will have access to HR services only afforded by some of the largest companies.</p>
    <p class="feature"><span class="feature-name">Library</span> – our online document library lets you and employees create your own library of information accessible at any time. Employees can upload documents and forms that can be kept in history as long as needed.</p>

    <h2 class="section-title">ACA COMPLIANCE</h2>
    <p class="feature"><span class="feature-name">Client Tools</span> – provide you with reporting and analysis tools online so you can monitor ACA information and be proactive in managing your needs.</p>
    <p class="feature"><span class="feature-name">Affordability Test</span> – provide your with information about plan affordability with their employees so they can stay in compliance.</p>
    <p class="feature"><span class="feature-name">Large Employer Analysis</span> – Analyze your control groups to determine if you will fall under the rules of ACA for large employer groups.</p>
  </section>

  <section class="panel panel--middle">
    <h2 class="section-title">BENEFIT ENROLLMENT</h2>
    <p class="feature"><span class="feature-name">Easy and Quick Enrollment</span> – our intuitive user experience quickly walks employees through their benefit enrollment process and allows them to compare different plans and select those that best meet their life needs.</p>
    <p class="feature"><span class="feature-name">Flexible Benefit Plans and Easy Setup Options</span> – Offer your clients Summit 500 benefit plans or administer their plans in an easy to use,<br>yet flexible benefit administration module.</p>
    <p class="feature"><span class="feature-name">You Pick</span> – with our flexible contribution setup features, you can contribute in any manner to your employees’ benefits while the system<br>automatically processes them through payroll</p>

    <h2 class="section-title">ON BOARDING</h2>
    <p class="feature"><span class="feature-name">Customize your On Boarding</span> – you can customize your on boarding experience to your hiring needs as well as provide multiple workflows for different employee types. The on boarding experience can be branded for you, providing a personalized experience for the employees.</p>
    <p class="feature"><span class="feature-name">Custom Document Management</span> – our custom document mapping feature lets you use your own forms and documents as part of the on boarding and hiring process. When these forms are completed – and electronically signed – they stay in history as long as needed.</p>
    <p class="feature"><span class="feature-name">Intuitive</span> – with a focus on the user experience, your employees will find it easy and quick to get on boarded with you.</p>

    <h2 class="section-title">WORKERS COMPENSATION &amp; BENEFITS</h2>
    <p class="feature"><span class="feature-name">Pay as you go Worker's Compensation</span> - Multiple carriers available.<br>Access to a Multiple Employer 401K &amp; to various voluntary benefits</p>

    <h2 class="section-title">TIME &amp; ATTENDANCE</h2>
    <p class="feature"><span class="feature-name">Make Time Entry Easy</span> – Simplify time tracking so you can spend less time on payroll tasks.</p>
    <p class="feature"><span class="feature-name">Everywhere Access</span> – Web interface, mobile apps, and on-premise time clocks allow employees to log their time wherever they are.</p>
    <p class="feature"><span class="feature-name">Plug &amp; Play Time Clocks</span> – Time clocks are delivered ready-to-use with little or no setup required.</p>
  </section>

  <section class="panel panel--right">
    <h2 class="section-title">APPLICANT TRACKING</h2>
    <p class="feature"><span class="feature-name">Create and Post Jobs</span> – you can create jobs with just a few clicks and post them on all the popular job sites.</p>
    <p class="feature"><span class="feature-name">Hire the Right People</span> – by posting on popular job boards, as well as a proprietary database of job seekers, you will reach more candidates. You can choose to receive profiles of candidates that only match your background<br>and specifications.</p>
    <p class="feature"><span class="feature-name">Manage the Hiring Process</span> – review candidates via video or online conferencing, review voice interviews, schedule in person interviews, have candidates answer certain online questions, and manage this entire process to find the right people. Once hired, they can be on boarded automatically.</p>

    <h2 class="section-title">SELF SERVICE</h2>
    <p class="feature"><span class="feature-name">Manager</span> – your managers have access to their information via a highly intuitive online portal. Users can enter payroll time, create ad-hoc reports, preview and approve payroll and invoices, get invoice and check history, access employee records, communicate with employees, create, etc. Our single sign on allows managers that may have multiple business entities with NORVALE umbrella to use one login.</p>
    <p class="feature"><span class="feature-name">Employee</span> – employees can access pay information, request PTO, enroll in benefits, communicate with other employees, and access/change their personal information. They can also access corporate documents for review and upload personal documents as well.</p>

    <h2 class="section-title">WOTC</h2>
    <p class="feature"><span class="feature-name">Big Credits</span> – Work Opportunity Tax Credits (WOTC) allow you to receive between $2,400 and $9,600 for hiring eligible employees</p>
    <p class="feature"><span class="feature-name">Easy &amp; Quick</span> – Employees complete a simple questionnaire to determine eligibility for WOTC. All of the necessary filing and reporting is handled for you and your client.</p>
    <p class="feature"><span class="feature-name">Integrated</span> – WOTC is integrated wherever you would enter a new employee – back office payroll, online on boarding, and applicant tracking to ensure all employees are being evaluated.</p>
  </section>
</main>
</body>
</html>
```